BriMora Journeys Business Card Design

We need a new business card design for our travel agency business - BriMora Journeys. We design packages to some of the most popular travel destinations in the world for groups, individuals and also tailor-make personalised packages. Our logo attached must be used. On the back of the card we would like a list of all websites under our BriMora brand to be posted. We would like clean, modern, simple design.

Industry/Entity Type

Travel Agent

Contact Information for Business Card

Owen Farrant
National Sales Manager
Reservations: 1300 527 649
Tel: 61 28473 5961
Fax: 61 2847 3907
Email: owen@brimorajourneys.com.au
Web: www.brimorajourneys.com.au

Address: Level 1, 417 Harwood Street
Sydney NSW 2000 Australia

Requirements
Must have
• On the back of the card we want all websites listed under our BriMora brand.
• BriMora Journeys Group - Wholesale Specialists
• www.kpwander.com.au - New Caledonia
• www.islebreeze.com.au - Tahiti
• www.orientjourneyhub.com.au - China
Nice to have
• Modern, clean lined, simple and fresh
Should not have
• Look dull

```html
<!DOCTYPE html>
<html lang="en">
<head>
<meta charset="utf-8">
<title>BriMora Journeys Business Card</title>
<link rel="stylesheet" href="https://fonts.googleapis.com/css2?family=Open+Sans:wght@400;600;700;800&display=swap">
<style>
  :root {
    --navy: #2d2a7f;
    --red: #e8282b;
    --ink: #2b2b2b;
    --rule: #c9c9d2;
    --paper: #ffffff;
    --backdrop: #d9d9dc;
  }
  * { box-sizing: border-box; margin: 0; padding: 0; }
  html, body { width: 1200px; height: 900px; overflow: hidden; }
  body {
    background: var(--backdrop);
    font-family: "Open Sans", Arial, sans-serif;
    display: flex; flex-direction: column; align-items: center; justify-content: center;
    gap: 36px;
  }
  .card {
    position: relative;
    width: 700px; height: 400px;
    box-shadow: 0 6px 18px rgba(0,0,0,.18);
  }
  .card--front { background: var(--paper); color: var(--ink); }
  .card--back { background: var(--navy); color: #fff; }

  .brand {
    position: absolute; left: 0; right: 0;
    display: flex; align-items: center; justify-content: center; gap: 14px;
  }
  .brand__rule { position: absolute; left: 190px; right: 190px; top: 0; height: 1px; }
  .brand__name { font-weight: 800; font-size: 50px; letter-spacing: -1px; line-height: 1; }
  .brand__dot { width: 18px; height: 18px; border-radius: 50%; }

  .card--front .brand { top: 52px; padding-top: 16px; }
  .card--front .brand__rule { background: var(--navy); }
  .card--front .brand__name { color: var(--navy); }
  .card--front .brand__dot { background: var(--red); }

  .card--front .divider {
    position: absolute; left: 40px; right: 40px; top: 152px; height: 1px; background: var(--rule);
  }

  .person { position: absolute; left: 46px; top: 184px; font-size: 15px; line-height: 1.45; }
  .person__name { font-weight: 700; font-size: 19px; color: var(--navy); }
  .person__name .surname { color: var(--red); }
  .person__title { margin-bottom: 14px; }

  .contact {
    position: absolute; right: 44px; top: 244px; width: 300px;
    border-top: 1px solid var(--rule); padding-top: 10px;
    font-size: 15px; line-height: 1.5;
  }
  .contact__label { color: var(--red); font-weight: 600; }
  .contact__row { display: flex; align-items: center; gap: 10px; }
  .contact__row svg { width: 13px; height: 13px; fill: var(--red); flex: none; }

  .card--back .brand { top: 80px; padding-top: 16px; }
  .card--back .brand__rule { background: rgba(255,255,255,.55); }
  .card--back .brand__dot { background: #fff; }
  .back-info {
    position: absolute; left: 0; right: 0; top: 178px;
    text-align: center; font-size: 15px; line-height: 1.5;
  }
  .back-info .group { margin-bottom: 14px; }
</style>
</head>
<body>

<section class="card card--front" aria-label="Business card front">
  <div class="brand">
    <span class="brand__rule"></span>
    <span class="brand__name">BriMora Journeys</span>
    <span class="brand__dot"></span>
  </div>
  <div class="divider"></div>

  <div class="person">
    <p class="person__name">Owen <span class="surname">Farrant</span></p>
    <p class="person__title">National Sales Manager</p>
    <p>Level 1, 417 Harwood Street</p>
    <p>Sydney NSW 2000 Australia</p>
  </div>

  <div class="contact">
    <p><span class="contact__label">Reservations:</span> 1300 527 649</p>
    <p class="contact__row">
      <svg viewBox="0 0 16 16" aria-label="Telephone"><path d="M3 1h3l1.5 4-2 1.3a9 9 0 0 0 4.2 4.2L11 8.5l4 1.5v3a2 2 0 0 1-2 2A12 12 0 0 1 1 3a2 2 0 0 1 2-2z"/></svg>
      61 28473 5961
    </p>
    <p class="contact__row">
      <svg viewBox="0 0 16 16" aria-label="Fax"><path d="M4 1h7l2 2v3H4z M1 7h14v8H1z M4 10h8v1H4z M4 12h8v1H4z" fill-rule="evenodd"/></svg>
      61 2847 3907
    </p>
    <p class="contact__row">
      <svg viewBox="0 0 16 16" aria-label="Email"><path d="M1 3h14v10H1z M1 3l7 6 7-6"/></svg>
      owen@brimorajourneys.com.au
    </p>
    <p class="contact__row">
      <svg viewBox="0 0 16 16" aria-label="Website"><path d="M6.5 9.5l3-3 M7 4l1.5-1.5a3 3 0 0 1 4.2 4.2L11 8.5 M9 12l-1.5 1.5a3 3 0 0 1-4.2-4.2L5 7.5" fill="none" stroke="#e8282b" stroke-width="2" stroke-linecap="round"/></svg>
      www.brimorajourneys.com.au
    </p>
  </div>
</section>

<section class="card card--back" aria-label="Business card back">
  <div class="brand">
    <span class="brand__rule"></span>
    <span class="brand__name">BriMora Journeys</span>
    <span class="brand__dot"></span>
  </div>
  <div class="back-info">
    <p>BriMora Journeys Group</p>
    <p class="group">Wholesale Specialists</p>
    <p>www.kpwander.com.au - New Caledonia</p>
    <p>www.islebreeze.com.au - Tahiti</p>
    <p>www.orientjourneyhub.com.au - China</p>
  </div>
</section>

</body>
</html>
```